Harborstone Flag Design

We are looking to design a flag that will be 3 feet tall by 5 feet wide. We want our logo to be on it (attached 2 options) . Colors will be black, white, and red. I would prefer to not have any background pictures. We are a mortgage company that specializes in VA (military) home loans. our website is www.harborstonelending.example. Something with an American Flag or parts of it would be ok, but not required. The only requirement is that our logo be on there and it must have some red. This flag will be mounted to a Kestrel TXR like the picture attached

```html
<!DOCTYPE html>
<html lang="en">
<head>
<meta charset="utf-8">
<title>Harborstone Flag Design</title>
<link rel="stylesheet" href="https://fonts.googleapis.com/css2?family=Playfair+Display:wght@700&display=swap">
<style>
  :root {
    --backdrop: #ececec;
    --flag-red: #be1e3c;
    --flag-white: #ffffff;
    --flag-navy: #1f2d5e;
    --flag-navy-light: #27376c;
    --ink: #111111;
  }
  * { box-sizing: border-box; margin: 0; padding: 0; }
  html, body {
    width: 980px;
    height: 1200px;
    overflow: hidden;
    background: var(--backdrop);
  }
  .canvas {
    width: 980px;
    height: 1200px;
    display: flex;
    align-items: center;
    justify-content: center;
  }
  .flag {
    width: 900px;
    height: 540px;
    display: flex;
    flex-direction: column;
    box-shadow: 6px 8px 14px rgba(0, 0, 0, 0.25);
  }
  .flag__band--red {
    height: 165px;
    background: var(--flag-red);
  }
  .flag__band--white {
    height: 206px;
    background: var(--flag-white);
    display: flex;
    align-items: center;
    justify-content: center;
  }
  .flag__band--navy {
    height: 169px;
    background: linear-gradient(180deg, var(--flag-navy-light), var(--flag-navy));
  }
  .brand {
    display: flex;
    align-items: center;
    gap: 28px;
    font-family: "Playfair Display", Georgia, serif;
    font-weight: 700;
    color: var(--ink);
  }
  .brand__square {
    width: 84px;
    height: 84px;
    background: var(--ink);
  }
  .brand__words {
    display: flex;
    flex-direction: column;
    align-items: center;
  }
  .brand__name {
    font-size: 72px;
    line-height: 1;
    letter-spacing: 4px;
    text-transform: uppercase;
  }
  .brand__suffix {
    margin-top: 12px;
    font-size: 20px;
    line-height: 1;
    letter-spacing: 13px;
    text-transform: uppercase;
  }
</style>
</head>
<body>
  <main class="canvas">
    <div class="flag">
      <div class="flag__band--red"></div>
      <div class="flag__band--white">
        <div class="brand">
          <div class="brand__square"></div>
          <div class="brand__words">
            <span class="brand__name">Harborstone</span>
            <span class="brand__suffix">Financial, LLC</span>
          </div>
        </div>
      </div>
      <div class="flag__band--navy" role="img" aria-label="Navy band with three rows of white stars"></div>
    </div>
  </main>
</body>
</html>
```